Email Banner: Brightfold

Need an email banner for https://brightfold-hub.io/ much the same design for the attatched just using the logo and brand as the guidance.

Tagline should be "Essential Whitepapers for Business Professionals" or "Whitepapers featured from the most reputable companies in the industry"

It will be going on an email that looks like this:

https://mailvista-demo.co/emails/preview/fullscreen/a71b3d2e-9c4f-4e8a-b12d-f05e6a8c1b3d

So dont make it to thick and clunky.

Target Market(s)

IT Proffesioanls

Industry/Entity Type

Information Technology

Logo Text

Essential Whitepapers for Business Professionals

Logo styles of interest
Abstract Logo
Font styles to use
Sans Serif

Colors
0054AA
0677BA
7BADD7
CADEEF
E8F1F8

Requirements
Must have
• Logo and colour scheme from the weblink provided: https://brightfold-hub.io/

```html
<!DOCTYPE html>
<html lang="en">
<head>
<meta charset="utf-8">
<title>Brightfold Email Banner</title>
<link rel="stylesheet" href="https://fonts.googleapis.com/css2?family=Plus+Jakarta+Sans:wght@400;700;800&display=swap">
<style>
  :root {
    --page-bg: #ffffff;
    --brand-blue: #0054AA;
    --ocean-blue: #0677BA;
    --sky-blue: #7BADD7;
    --pale-blue: #CADEEF;
    --ice-blue: #E8F1F8;
    --deep-navy: #003B7A;
    --ink-navy: #0A2342;
    --on-dark: #ffffff;
  }
  html, body {
    margin: 0;
    padding: 0;
    width: 1200px;
    height: 1200px;
    overflow: hidden;
    background: var(--page-bg);
    font-family: "Plus Jakarta Sans", sans-serif;
  }
  .email-banner {
    position: absolute;
    left: 177px;
    top: 532px;
    width: 845px;
    height: 135px;
    box-sizing: border-box;
    border: 1px solid var(--sky-blue);
    border-top: none;
    overflow: hidden;
  }
  .banner-shapes {
    position: absolute;
    inset: 0;
    width: 100%;
    height: 100%;
  }
  .brand {
    position: absolute;
    left: 34px;
    top: 67px;
    transform: translateY(-50%);
    display: flex;
    align-items: center;
    gap: 14px;
  }
  .brand-dot {
    width: 36px;
    height: 36px;
    border-radius: 50%;
    background: var(--brand-blue);
  }
  .brand-name {
    font-weight: 700;
    font-size: 33px;
    letter-spacing: -0.3px;
    color: var(--ink-navy);
  }
  .tagline {
    position: absolute;
    left: 403px;
    top: 38px;
    margin: 0;
    color: var(--on-dark);
    font-size: 22px;
    font-weight: 400;
    line-height: 31px;
    word-spacing: 1px;
    white-space: nowrap;
  }
  .tagline strong { font-weight: 700; }
  .cta {
    position: absolute;
    right: 18px;
    top: 11px;
    color: var(--on-dark);
    font-size: 15.5px;
    font-weight: 800;
    letter-spacing: 0.2px;
    text-decoration: none;
  }
</style>
</head>
<body>
  <div class="email-banner">
    <svg class="banner-shapes" viewBox="0 0 721 115" preserveAspectRatio="none" aria-hidden="true">
      <defs>
        <linearGradient id="blueFade" x1="0" y1="0" x2="1" y2="0" gradientUnits="objectBoundingBox">
          <stop offset="0" stop-color="var(--deep-navy)"/>
          <stop offset="0.35" stop-color="var(--brand-blue)"/>
          <stop offset="0.62" stop-color="var(--ocean-blue)"/>
          <stop offset="0.86" stop-color="var(--sky-blue)"/>
          <stop offset="1" stop-color="var(--ice-blue)"/>
        </linearGradient>
      </defs>
      <rect x="0" y="0" width="721" height="115" fill="var(--page-bg)"/>
      <path d="M319,6 L721,6 L721,115 L235,115 C262,113 278,100 289,76 Z" fill="url(#blueFade)"/>
      <rect x="0" y="0" width="721" height="6" fill="var(--brand-blue)"/>
      <path d="M598,0 L721,0 L721,35 L642,35 C626,35 619,26 613,16 C608,8 604,3 598,0 Z" fill="var(--brand-blue)"/>
    </svg>

    <div class="brand">
      <span class="brand-dot"></span>
      <span class="brand-name">Brightfold</span>
    </div>

    <p class="tagline">Essential Whitepapers<br>for <strong>Business Professionals</strong></p>

    <a class="cta" href="https://brightfold-hub.io/">CLICK HERE</a>
  </div>
</body>
</html>
```